Logo and Business Card Design

We are macadamia farmers with a network of operations able to deliver macadamia nuts to you!
Be it wholesale or retail supply, our production capacity, network of farms and processing facilities is able to provide reliable and secure supply of macadamia products.
We have a network of owned and contract production macadamia farms located throughout Queensland and New South Wales. Our farms are located in the lush green hinterland area of Northern New south wales and the rich and productive farmlands of the Burnett area of southern Queensland. We pride ourselves on our environmentally sensitive production systems, the ownership and pride in which our network of farmers care for their orchards and the food we produce. Collectively our farms deliver to processing facilities able to provide macadamia nut in shell and kernel in wholesale and retail quantities.
Our point of difference is our integrated supply chain, delivering paddock to plate capacity.
The enterprise is a true network in that we have combined production, processing and marketing expertise into a one stop shop!
Our design should communicate our network capacity, we are a food producer which is respectful of the land and the environment in which we operate.
Our focus is Macadamia nut production, we farm and process Macadamia's where they are a native tree.

The draft design concept we feel is too mechanical and sterile, its time for something fresh and exciting!

Environment

Tellow Grove Pty. Ltd
An Integrated Macadamia production Enterprise.

```html
<!DOCTYPE html>
<html lang="en">
<head>
<meta charset="utf-8">
<title>Tellow Grove – Business Card</title>
<link rel="stylesheet" href="https://fonts.googleapis.com/css2?family=Exo+2:wght@400;500;800&display=swap">
<style>
  :root {
    --bg: #e7e4df;
    --card: #ffffff;
    --brown: #3f2416;
    --green: #1f9a48;
    --ink: #3a2418;
    --light: #f4efe9;
    --shadow: rgba(40, 25, 15, 0.18);
  }
  * { box-sizing: border-box; margin: 0; padding: 0; }
  html, body { width: 1200px; height: 900px; overflow: hidden; }
  body {
    background: var(--bg);
    font-family: "Exo 2", sans-serif;
    position: relative;
  }
  .card {
    position: absolute;
    left: 250px;
    width: 700px;
    height: 400px;
    background: var(--card);
    border-radius: 30px;
    overflow: hidden;
    box-shadow: 0 10px 28px var(--shadow);
  }
  .card--front { top: 35px; }
  .card--back { top: 465px; }

  .card__band { position: absolute; inset: 0; width: 100%; height: 100%; }

  .brand {
    position: absolute;
    display: flex;
    align-items: center;
    gap: 14px;
    color: var(--ink);
    font-weight: 800;
    text-transform: uppercase;
    line-height: 0.95;
    letter-spacing: 1px;
  }
  .brand__dot {
    width: 22px; height: 22px;
    border-radius: 50%;
    background: var(--green);
    flex: none;
  }
  .card--front .brand { left: 42px; top: 42px; font-size: 44px; }
  .card--back .brand { left: 50%; top: 50%; transform: translate(-50%, -50%); font-size: 62px; gap: 20px; }
  .card--back .brand__dot { width: 30px; height: 30px; }

  .person {
    position: absolute;
    right: 52px;
    top: 98px;
    text-align: right;
    color: var(--ink);
  }
  .person__name { font-size: 23px; font-weight: 500; letter-spacing: 1.5px; text-transform: uppercase; }
  .person__role { font-size: 16px; margin-top: 4px; }

  .contact {
    position: absolute;
    right: 48px;
    top: 272px;
    list-style: none;
    color: var(--light);
    font-size: 14px;
    text-align: right;
  }
  .contact__item {
    display: flex;
    justify-content: flex-end;
    align-items: center;
    gap: 8px;
    height: 20px;
  }
  .contact__icon { width: 13px; height: 13px; fill: var(--light); flex: none; }

  .address {
    position: absolute;
    left: 42px;
    bottom: 26px;
    color: var(--light);
    font-size: 16px;
    letter-spacing: 0.5px;
  }
</style>
</head>
<body>

<section class="card card--front" aria-label="Business card front">
  <svg class="card__band" viewBox="0 0 700 400" preserveAspectRatio="none" aria-hidden="true">
    <path d="M0,176 Q330,112 700,252" fill="none" stroke="var(--green)" stroke-width="7"/>
    <path d="M0,192 Q330,128 700,268 L700,400 L0,400 Z" fill="var(--brown)"/>
  </svg>

  <div class="brand">
    <span class="brand__name">Tellow<br>Grove</span>
    <span class="brand__dot"></span>
  </div>

  <div class="person">
    <p class="person__name">Daniel Hargreave</p>
    <p class="person__role">Managing Director</p>
  </div>

  <ul class="contact">
    <li class="contact__item">07 4100 2233
      <svg class="contact__icon" viewBox="0 0 24 24"><path d="M6.6 10.8a15.1 15.1 0 0 0 6.6 6.6l2.2-2.2c.3-.3.7-.4 1-.2 1.1.4 2.3.6 3.6.6.6 0 1 .4 1 1V20c0 .6-.4 1-1 1A17 17 0 0 1 3 4c0-.6.4-1 1-1h3.5c.6 0 1 .4 1 1 0 1.3.2 2.5.6 3.6.1.3 0 .7-.2 1z"/></svg>
    </li>
    <li class="contact__item">0412 556 780
      <svg class="contact__icon" viewBox="0 0 24 24"><path d="M7 1h10a2 2 0 0 1 2 2v18a2 2 0 0 1-2 2H7a2 2 0 0 1-2-2V3a2 2 0 0 1 2-2zm0 3v14h10V4zm5 15.5a1.2 1.2 0 1 0 0 2.4 1.2 1.2 0 0 0 0-2.4z"/></svg>
    </li>
    <li class="contact__item">07 4100 2234
      <svg class="contact__icon" viewBox="0 0 24 24"><path d="M6 2h9l4 4v4h1a2 2 0 0 1 2 2v8a2 2 0 0 1-2 2H4a2 2 0 0 1-2-2v-8a2 2 0 0 1 2-2h2zm2 2v6h9V7h-3V4zm-2 9v2h4v-2zm0 4v2h4v-2zm8-4v6h5v-6z"/></svg>
    </li>
    <li class="contact__item">www.tellowgrove.com
      <svg class="contact__icon" viewBox="0 0 24 24"><path d="M3 5h18a1 1 0 0 1 1 1v12a1 1 0 0 1-1 1H3a1 1 0 0 1-1-1V6a1 1 0 0 1 1-1zm0 2v1l9 5 9-5V7l-9 5z"/></svg>
    </li>
    <li class="contact__item">hello@tellowgrove.com
      <svg class="contact__icon" viewBox="0 0 24 24"><path d="M12 2a10 10 0 1 0 0 20 10 10 0 0 0 0-20zm0 2c.9 0 2.2 1.8 2.8 5H9.2C9.8 5.8 11.1 4 12 4zM4.3 11h2.9a19 19 0 0 0 0 2H4.3a8 8 0 0 1 0-2zm4.9 0h5.6a17 17 0 0 1 0 2H9.2a17 17 0 0 1 0-2zm7.6 0h2.9a8 8 0 0 1 0 2h-2.9a19 19 0 0 0 0-2zM9.2 15h5.6c-.6 3.2-1.9 5-2.8 5s-2.2-1.8-2.8-5z"/></svg>
    </li>
  </ul>

  <p class="address">14 Orchard Ridge Road Bundaberg QLD</p>
</section>

<section class="card card--back" aria-label="Business card back">
  <div class="brand">
    <span class="brand__name">Tellow<br>Grove</span>
    <span class="brand__dot"></span>
  </div>
</section>

</body>
</html>
```